Meadowlark Crest Brochure

I need an A4 size brochure, A front and a back. All the information needed on the brochure can be found in this link:

https://www.filevinto.com/s/8kq52zt04mxa7c3/OWEN%20HARLOW.rar?dl=0

If you have questions, do not hesitate to ask.

```html
<!DOCTYPE html>
<html lang="en">
<head>
<meta charset="utf-8">
<title>Meadowlark Crest – Our Aim</title>
<link href="https://fonts.googleapis.com/css2?family=Arimo:wght@400;700&display=swap" rel="stylesheet">
<style>
  :root {
    --sea-light: #41c6f0;
    --sea-mid: #1aa9e4;
    --sea-deep: #0c8fd3;
    --sky: #e6f4fb;
    --sky-blue: #bfe3f5;
    --palm-dark: #23401a;
    --palm: #4f7d2c;
    --palm-light: #93b95c;
    --band: #c0704d;
    --band-dark: #9e5539;
    --logo-brown: #77604f;
    --leaf: #8fc741;
    --leaf-light: #bfe07e;
    --rock: #3a3a38;
    --soil: #5a4430;
    --white: #ffffff;
  }
  html, body {
    margin: 0;
    padding: 0;
    overflow: hidden;
    background: #e9ecef;
  }
  .brochure {
    position: relative;
    width: 848px;
    height: 1200px;
    overflow: hidden;
    background: linear-gradient(180deg, var(--sea-light) 0%, var(--sea-light) 45%, var(--sea-mid) 62%, var(--sea-deep) 78%, var(--sea-mid) 100%);
    font-family: "Arimo", Arial, sans-serif;
    color: var(--white);
  }
  .hero-photo {
    position: absolute;
    left: 0; top: 0;
    width: 848px; height: 520px;
    background:
      linear-gradient(180deg, rgba(65,198,240,0) 82%, var(--sea-light) 100%),
      linear-gradient(180deg, rgba(0,0,0,0) 0%, rgba(0,0,0,0) 86%, rgba(120,210,240,0.9) 90%, var(--sea-light) 100%),
      radial-gradient(ellipse 260px 200px at 120px 110px, var(--palm-dark) 0%, rgba(35,64,26,0) 100%),
      radial-gradient(ellipse 300px 180px at 380px 90px, var(--palm) 0%, rgba(79,125,44,0) 100%),
      radial-gradient(ellipse 160px 130px at 760px 60px, rgba(79,125,44,0.85) 0%, rgba(79,125,44,0) 100%),
      radial-gradient(ellipse 240px 160px at 200px 330px, rgba(79,125,44,0.9) 0%, rgba(79,125,44,0) 100%),
      linear-gradient(90deg, var(--palm-dark) 0%, var(--palm) 25%, var(--palm-light) 45%, var(--sky-blue) 62%, var(--sky) 85%, var(--sky-blue) 100%);
  }
  .shore-photo {
    position: absolute;
    left: 0; top: 900px;
    width: 848px; height: 300px;
    background:
      linear-gradient(180deg, var(--sea-deep) 0%, rgba(12,143,211,0) 18%),
      radial-gradient(ellipse 230px 120px at 130px 150px, var(--rock) 0%, rgba(58,58,56,0) 100%),
      radial-gradient(ellipse 200px 110px at 640px 230px, rgba(60,40,28,0.9) 0%, rgba(60,40,28,0) 100%),
      linear-gradient(180deg, #7ccbe6 0%, #a6dcea 22%, #89b8b6 38%, #6b6a60 52%, var(--soil) 72%, #3a2c1f 100%);
  }
  .bands {
    position: absolute;
    left: 0; top: 0;
  }
  .logo-badge {
    position: absolute;
    left: 523px; top: 174px;
    width: 260px; height: 260px;
    border-radius: 50%;
    background: var(--logo-brown);
    border: 7px solid var(--white);
    box-sizing: border-box;
    display: flex;
    align-items: center;
    justify-content: center;
    text-align: center;
  }
  .logo-name {
    margin: 0;
    font-size: 36px;
    font-weight: 700;
    line-height: 1.05;
    color: var(--white);
  }
  .bird-photo {
    position: absolute;
    left: 100px; top: 366px;
    width: 202px; height: 202px;
    border-radius: 50%;
    border: 5px solid var(--band);
    box-sizing: border-box;
    background:
      radial-gradient(ellipse 60px 80px at 42% 42%, #3f6fc8 0%, rgba(63,111,200,0) 100%),
      radial-gradient(ellipse 70px 40px at 45% 78%, #6a5a46 0%, rgba(106,90,70,0) 100%),
      radial-gradient(circle at 50% 50%, #4a4236 0%, #2a241d 70%, #1b1713 100%);
  }
  .leaf-icon {
    position: absolute;
    left: 368px; top: 478px;
  }
  .aim {
    position: absolute;
    left: 54px; top: 568px;
    width: 740px;
  }
  .aim-kicker {
    margin: 0;
    text-align: center;
    font-size: 24px;
    font-weight: 700;
    line-height: 30px;
  }
  .aim-title {
    margin: 2px 0 16px;
    text-align: center;
    font-size: 42px;
    font-weight: 700;
    line-height: 48px;
  }
  .aim-text {
    margin: 0 0 12px;
    font-size: 18px;
    font-weight: 700;
    line-height: 24.7px;
  }
  .line {
    display: block;
    white-space: nowrap;
    text-align: justify;
    text-align-last: justify;
  }
  .line-end {
    display: block;
    text-align: left;
  }
  .site-url {
    position: absolute;
    left: 0; top: 1143px;
    width: 848px;
    margin: 0;
    text-align: center;
    font-size: 21px;
    font-weight: 700;
    letter-spacing: 0.6px;
  }
</style>
</head>
<body>
<div class="brochure">
  <div class="hero-photo" role="img" aria-label="Tropical beach with tall palm trees, pale blue sky and a long wooden jetty stretching over turquoise sea"></div>
  <div class="shore-photo" role="img" aria-label="Rocky shoreline by clear water with butterflies resting on the ground"></div>

  <svg class="bands" width="848" height="1200" viewBox="0 0 848 1200" aria-hidden="true">
    <path d="M-10 458 C 120 450, 240 430, 330 385 S 470 280, 560 250 S 760 195, 860 186" fill="none" stroke="var(--band)" stroke-width="20"/>
    <path d="M-10 1080 C 160 1072, 330 1040, 480 1022 S 740 1006, 860 1000" fill="none" stroke="var(--band)" stroke-width="26"/>
    <path d="M-10 1096 C 160 1088, 330 1056, 480 1038 S 740 1020, 860 1015" fill="none" stroke="var(--band-dark)" stroke-width="3" opacity="0.6"/>
  </svg>

  <div class="bird-photo" role="img" aria-label="Blue kingfisher perched on a branch"></div>

  <div class="logo-badge">
    <p class="logo-name">Meadowlark<br>Crest</p>
  </div>

  <svg class="leaf-icon" width="112" height="86" viewBox="0 0 112 86" aria-hidden="true">
    <path d="M53 84 C 22 78, 6 48, 12 4 C 44 18, 60 48, 53 84 Z" fill="var(--leaf)"/>
    <path d="M59 84 C 90 78, 106 48, 100 4 C 68 18, 52 48, 59 84 Z" fill="var(--leaf-light)"/>
  </svg>

  <section class="aim">
    <p class="aim-kicker">Our Aim.</p>
    <h1 class="aim-title">Preserving the Environment!</h1>
    <p class="aim-text">
      <span class="line">The entire tour has been constructed to show guests the importance of</span>
      <span class="line">conservation with our rainforest. We will provide an exclusive Rainforest</span>
      <span class="line">experience without causing and damage to the fragile rainforest</span>
      <span class="line">ecosystem. Our aim is to protect this precious environment and</span>
      <span class="line">encourage others to do the same. Our tour is also focused on the</span>
      <span class="line">importance Aboriginal culture and keeping it alive for many generations</span>
      <span class="line-end">to come!</span>
    </p>
    <p class="aim-text">
      <span class="line">Leave nothing but your footsteps, and take nothing but priceless</span>
      <span class="line-end">photographs.</span>
    </p>
  </section>

  <p class="site-url">www.meadowlarkcrest.com.au</p>
</div>
</body>
</html>
```